Trading Company needs a business card design, letter head design and email signature

We need a double-sided business card design, letter head design and an email signature. We have a logo design.

Possible Tag Lines:
• “Connecting Worlds, Building Excellence.”
• “Global Sourcing, Local Excellence.”
• “Bridging Borders, Building Quality.”
• “Worldwide Partnerships, Superior Goods.”
• “Where Quality Meets Affordability”

Services Offered:
Procurement
Fabrication
Distribution
Logistics
Import/Export

Requirements
Must have
• Nice quality double sided Business Card design, Letterhead design needs to be A4
Nice to have
• possible ideas on tag lines

```html
<!DOCTYPE html>
<html lang="en">
<head>
<meta charset="utf-8">
<title>Corvane Letterhead</title>
<link href="https://fonts.googleapis.com/css2?family=Montserrat:wght@400;600&family=Source+Sans+3:wght@400&display=swap" rel="stylesheet">
<style>
  :root {
    --backdrop: #dedede;
    --paper: #f8f8f8;
    --brand-red: #e52225;
    --rule-red: #e8575b;
    --slate: #585a5c;
    --ink: #5a5a5a;
    --signature-tone: #e6e8ee;
  }
  * { box-sizing: border-box; margin: 0; padding: 0; }
  html, body {
    width: 1153px;
    height: 1200px;
    overflow: hidden;
    background: var(--backdrop);
  }
  .letterhead {
    position: absolute;
    left: 160px;
    top: 20px;
    width: 833px;
    height: 1160px;
    background: var(--paper);
    box-shadow: 0 6px 18px rgba(0,0,0,0.12);
    overflow: hidden;
  }
  .brand {
    position: absolute;
    left: 89px;
    top: 150px;
    width: 166px;
    display: flex;
    align-items: center;
    justify-content: center;
    gap: 7px;
  }
  .brand-mark {
    width: 12px;
    height: 12px;
    background: var(--brand-red);
  }
  .brand-name {
    font-family: "Montserrat", sans-serif;
    font-weight: 600;
    font-size: 23px;
    letter-spacing: 1.5px;
    line-height: 1;
    color: var(--brand-red);
  }
  .contact {
    position: absolute;
    left: 585px;
    top: 73px;
    font-family: "Montserrat", sans-serif;
    font-style: normal;
    font-size: 13px;
    color: var(--ink);
    line-height: 16px;
  }
  .contact-address { margin-bottom: 10px; }
  .contact-line {
    display: flex;
    align-items: center;
    gap: 5px;
    height: 17px;
  }
  .contact-icon { width: 12px; height: 12px; flex: none; }
  .header-rule {
    position: absolute;
    left: 83px;
    top: 201px;
    width: 664px;
    height: 1px;
    background: var(--rule-red);
  }
  .letter-body {
    position: absolute;
    left: 83px;
    top: 274px;
    width: 668px;
    font-family: "Source Sans 3", sans-serif;
    font-size: 15.3px;
    line-height: 21.9px;
    color: var(--ink);
  }
  .letter-body p {
    text-align: justify;
    text-align-last: left;
    margin-bottom: 21.9px;
  }
  .salutation { margin-bottom: 21.9px; }
  .signature {
    position: absolute;
    left: 83px;
    top: 848px;
    width: 97px;
    height: 91px;
    background: var(--signature-tone);
  }
  .footer-band {
    position: absolute;
    left: 0;
    bottom: 0;
    width: 833px;
    height: 13px;
  }
</style>
</head>
<body>
  <main class="letterhead">
    <header>
      <div class="brand">
        <span class="brand-mark"></span>
        <span class="brand-name">CORVANE</span>
      </div>

      <address class="contact">
        <div class="contact-address">48 Harbor Lane Suite<br>7 Millbrook, MA 01920</div>
        <div class="contact-line">
          <svg class="contact-icon" viewBox="0 0 24 24" aria-hidden="true"><path fill="#e52225" d="M6.6 10.8a15.1 15.1 0 0 0 6.6 6.6l2.2-2.2a1 1 0 0 1 1-.25 11.4 11.4 0 0 0 3.6.57 1 1 0 0 1 1 1V20a1 1 0 0 1-1 1A17 17 0 0 1 3 4a1 1 0 0 1 1-1h3.5a1 1 0 0 1 1 1c0 1.25.2 2.45.57 3.6a1 1 0 0 1-.25 1z"/></svg>
          <span>(555) 318-4072</span>
        </div>
        <div class="contact-line">
          <svg class="contact-icon" viewBox="0 0 24 24" aria-hidden="true"><rect x="2" y="5" width="20" height="14" fill="none" stroke="#e52225" stroke-width="2"/><path d="M2 5l10 8 10-8M2 19l7-7M22 19l-7-7" fill="none" stroke="#e52225" stroke-width="2"/></svg>
          <span>info@corvanemail.com</span>
        </div>
        <div class="contact-line">
          <svg class="contact-icon" viewBox="0 0 24 24" aria-hidden="true"><g fill="none" stroke="#e52225" stroke-width="1.8"><circle cx="12" cy="12" r="9.5"/><ellipse cx="12" cy="12" rx="4.5" ry="9.5"/><path d="M2.5 12h19M4 7h16M4 17h16"/></g></svg>
          <span>www.corvaneweb.com</span>
        </div>
      </address>
    </header>

    <div class="header-rule"></div>

    <section class="letter-body">
      <div class="salutation">Dear customer,</div>
      <p>Lorem ipsum dolor sit amet, consectetur adipisicing elit, sed do eiusmod tempor incididunt ut labore et dolore magna aliqua. Ut enim ad minim veniam, quis nostrud exercitation ullamco laboris nisi ut aliquip ex ea commodo consequat. Duis aute irure dolor in reprehenderit in voluptate velit esse cillum dolore eu fugiat nulla pariatur. Excepteur sint occaecat cupidatat non proident, sunt in culpa qui officia deserunt mollit anim id est laborum.</p>
      <p>Lorem ipsum dolor sit amet, consectetur adipisicing elit, sed do eiusmod tempor incididunt ut labore et dolore magna aliqua. Ut enim ad minim veniam, quis nostrud exercitation ullamco laboris nisi ut aliquip ex ea commodo consequat. Duis aute irure dolor in reprehenderit in voluptate velit esse cillum dolore eu fugiat nulla pariatur. Excepteur sint occaecat cupidatat non proident, sunt in culpa qui officia deserunt mollit anim id est laborum.</p>
      <p>Lorem ipsum dolor sit amet, consectetur adipisicing elit, sed do eiusmod tempor incididunt ut labore et dolore magna aliqua. Ut enim ad minim veniam, quis nostrud exercitation ullamco laboris nisi ut aliquip ex ea commodo consequat. Duis aute irure dolor in reprehenderit in voluptate velit esse cillum dolore eu fugiat nulla pariatur. Excepteur sint occaecat cupidatat non proident, sunt in culpa qui officia deserunt mollit anim id est laborum.</p>
      <p>Lorem ipsum dolor sit amet, consectetur adipisicing elit, sed do eiusmod tempor incididunt ut labore et dolore magna aliqua. Ut enim ad minim veniam, quis nostrud exercitation ullamco laboris nisi ut aliquip ex ea commodo consequat. Duis aute irure dolor in reprehenderit.</p>
      <div class="closing">Yours Sincerely,</div>
    </section>

    <div class="signature" role="img" aria-label="Handwritten signature of the sender"></div>

    <svg class="footer-band" viewBox="0 0 833 13" preserveAspectRatio="none" aria-hidden="true">
      <polygon points="0,0 630,0 617,13 0,13" fill="#e52225"/>
      <polygon points="638,0 833,0 833,13 625,13" fill="#585a5c"/>
    </svg>
  </main>
</body>
</html>
```